Mobile Oil Change company needs a flyer to promote new business

We need a flyer to 1) print & handout and 2) email out to potential customers. We are a mobile oil change company that comes to our customer locations to perform the work instead of customers going to traditional oil change companies. We have a 21 point inspection with our oil change. (21 point inspection details will not be on the flyer). Would like to keep the flyer simple but creative. I'm attaching 1) the write-up we created, 2) our logo (logo color is dark teal on white but other combinations are included if you wanted to propose a different color combination), and 3) additional services we offer. Logo font is Alegreya Sans.
Would like the additional services listed with icons and brief descriptions (similar to attachment) without pricing. Company website for reference is www.brookmerelubeworks.com.

Target Market(s)

Companies with many service vehicles such as Oil & Gas service companies, heating and air conditioning companies, utility companies, police departments, etc. Companies that prioritize convenience and maintenance first.

Font styles to use
Sans Serif

Colors
00a990

Requirements
Must have
• Simple but creative design with our logo at top of the flyer. Additional Services (details in document supplied) can be smaller and less prominent than other "main" content listed in the CONTENT document supplied.
Should not have
• Do not use animated character graphics in the flyer and limit (1) stock photos to A small area in the flyer.

```html
<!DOCTYPE html>
<html lang="en">
<head>
<meta charset="utf-8">
<title>Brookmere Lube Works – Mobile Oil Change Flyer</title>
<link rel="stylesheet" href="https://fonts.googleapis.com/css2?family=Roboto:wght@400;500;700;900&display=swap">
<style>
  :root {
    --teal: #00a990;
    --ink: #231f20;
    --ink-soft: #2d2a2b;
    --white: #ffffff;
    --stage: #e6e6e6;
    --rule: #d9d9d9;
    --font: "Roboto", Arial, sans-serif;
  }
  * { box-sizing: border-box; margin: 0; padding: 0; }
  html, body { width: 1200px; height: 800px; overflow: hidden; }
  body { background: var(--stage); font-family: var(--font); position: relative; }

  .flyer {
    position: absolute; left: 335px; top: 20px;
    width: 530px; height: 760px;
    background: var(--ink); overflow: hidden;
    box-shadow: 0 6px 18px rgba(0,0,0,.18);
  }
  .flyer-shapes { position: absolute; inset: 0; }
  .abs { position: absolute; }

  /* header */
  .brand {
    left: 52px; top: 30px; color: var(--white);
    font-weight: 700; font-size: 24px; line-height: 1.05; letter-spacing: 1.5px;
    text-transform: uppercase; display: flex; align-items: center; gap: 10px;
  }
  .brand-dot { width: 14px; height: 14px; border-radius: 50%; background: var(--teal); }
  .contact { left: 372px; top: 46px; width: 152px; color: var(--white); }
  .contact-icon { position: absolute; left: -2px; top: 0; width: 34px; height: 30px; }
  .contact-label { margin-left: 40px; font-weight: 700; font-size: 15px; line-height: 20px; }
  .contact-phone { margin-top: 4px; font-weight: 700; font-size: 17.5px; white-space: nowrap; margin-left: -38px; }

  /* hero */
  .hero-photo {
    left: 0; top: 114px; width: 530px; height: 262px;
    background:
      radial-gradient(ellipse 90px 130px at 245px 90px, rgba(214,160,40,.85), rgba(150,95,20,.35) 60%, transparent 80%),
      radial-gradient(ellipse 180px 110px at 330px 200px, #3c3b3c, transparent 75%),
      linear-gradient(100deg, #0f0f10 0%, #1d1d1e 40%, #48484a 70%, #2a2a2b 100%);
  }
  .headline {
    left: 26px; top: 180px; color: var(--white);
    font-weight: 700; font-size: 25px; line-height: 32px; text-transform: uppercase;
  }
  .headline-rule { left: 26px; top: 284px; width: 152px; height: 4px; background: var(--teal); }
  .subhead {
    left: 26px; top: 298px; color: var(--white);
    font-weight: 700; font-size: 15px; line-height: 20px; text-transform: uppercase;
  }

  /* process */
  .process-intro {
    left: 30px; top: 412px; width: 262px; color: var(--white);
    font-weight: 700; font-size: 13px; line-height: 15.5px;
  }
  .steps { left: 30px; top: 461px; list-style: none; display: flex; flex-direction: column; gap: 14px; }
  .step { display: flex; align-items: center; gap: 10px; height: 34px; }
  .step-num {
    flex: none; width: 28px; height: 28px; border-radius: 50%;
    background: var(--ink); border: 2px solid var(--white); color: var(--white);
    font-weight: 700; font-size: 16px; display: flex; align-items: center; justify-content: center;
  }
  .step-text { color: var(--ink); font-weight: 700; font-size: 12px; line-height: 13.5px; text-transform: uppercase; width: 200px; }

  /* highlights */
  .highlights { left: 328px; top: 412px; list-style: none; display: flex; flex-direction: column; gap: 12px; }
  .highlight { display: flex; gap: 12px; align-items: flex-start; color: var(--white); font-size: 12.5px; line-height: 14px; width: 196px; }
  .highlight svg { flex: none; width: 22px; height: 22px; margin-top: 2px; }

  /* additional services */
  .extras-title { left: 341px; top: 530px; color: var(--teal); font-weight: 700; font-size: 15.5px; text-transform: uppercase; }
  .extras { left: 344px; top: 562px; list-style: none; }
  .extra {
    display: flex; align-items: center; gap: 8px; height: 20.5px;
    color: var(--ink); font-weight: 700; font-size: 10px; text-transform: uppercase;
  }
  .extra:nth-child(2) { margin-left: -5px; }
  .extra:nth-child(3) { margin-left: -10px; }
  .extra:nth-child(4) { margin-left: -15px; }
  .extra:nth-child(5) { margin-left: -20px; }
  .extra:nth-child(6) { margin-left: -25px; }
  .extra svg { flex: none; width: 13px; height: 13px; }

  /* footer */
  .footer-item { display: flex; align-items: center; gap: 9px; color: var(--white); font-size: 11.5px; top: 727px; }
  .footer-item svg { width: 20px; height: 20px; }
  .footer-web { left: 38px; }
  .footer-mail { left: 282px; }
</style>
</head>
<body>
<article class="flyer">
  <svg class="flyer-shapes" width="530" height="760" viewBox="0 0 530 760" aria-hidden="true">
    <rect x="0" y="0" width="530" height="108" fill="var(--ink)"/>
    <polygon points="0,104 340,104 352,110 530,110 530,116 0,116" fill="var(--white)"/>
    <polygon points="374,36 530,36 530,104 350,104" fill="var(--teal)"/>
    <rect x="0" y="374" width="530" height="10" fill="var(--white)"/>
    <polygon points="7,398 300,398 300,560 276,704 7,704" fill="var(--teal)"/>
    <polygon points="322,518 530,518 530,704 296,704" fill="var(--white)"/>
    <polygon points="0,704 530,704 530,710 0,710" fill="var(--rule)"/>
    <polygon points="262,710 530,710 530,760 248,760" fill="var(--teal)"/>
  </svg>

  <header>
    <div class="abs brand"><span class="brand-dot"></span><span>Brookmere<br>Lube Works</span></div>
    <div class="abs contact">
      <svg class="contact-icon" viewBox="0 0 34 30" aria-hidden="true">
        <path d="M3 3h18v12H11l-5 4v-4H3z" fill="none" stroke="#fff" stroke-width="2" stroke-linejoin="round"/>
        <path d="M24 9h7v12h-3v4l-5-4h-9v-3" fill="none" stroke="#fff" stroke-width="2" stroke-linejoin="round"/>
        <circle cx="8" cy="9" r="1.4" fill="#fff"/><circle cx="12" cy="9" r="1.4" fill="#fff"/><circle cx="16" cy="9" r="1.4" fill="#fff"/>
      </svg>
      <p class="contact-label">CONTACT US:</p>
      <p class="contact-phone">(833) 555-0148</p>
    </div>
  </header>

  <section>
    <div class="abs hero-photo" role="img" aria-label="Photo of golden motor oil being poured from a bottle into an engine filler neck"></div>
    <h1 class="abs headline">Hassle free<br>oil changes<br>on your terms</h1>
    <div class="abs headline-rule"></div>
    <p class="abs subhead">Save time, money &amp;<br>avoid headaches!</p>
  </section>

  <section>
    <p class="abs process-intro">Our simple 5-step process lets you schedule an appointment and get service to save time and money:</p>
    <ol class="abs steps">
      <li class="step"><span class="step-num">1</span><span class="step-text">Call or email us to schedule service</span></li>
      <li class="step"><span class="step-num">2</span><span class="step-text">Our highly trained technicians come to you for service</span></li>
      <li class="step"><span class="step-num">3</span><span class="step-text">Service is performed quickly on your vehicle</span></li>
      <li class="step"><span class="step-num">4</span><span class="step-text">Pay agreed-upon pricing and receipt is emailed to you</span></li>
      <li class="step"><span class="step-num">5</span><span class="step-text">Services performed are tracked electronically and reminders created</span></li>
    </ol>

    <ul class="abs highlights">
      <li class="highlight">
        <svg viewBox="0 0 22 22" aria-hidden="true"><circle cx="11" cy="11" r="9.5" fill="none" stroke="#fff" stroke-width="1.8"/><path d="M6.5 11.3l3 3 6-6.3" fill="none" stroke="#fff" stroke-width="2"/></svg>
        <span>High quality synthetic oil used is best suited for commercial vehicles</span>
      </li>
      <li class="highlight">
        <svg viewBox="0 0 22 22" aria-hidden="true"><circle cx="11" cy="11" r="9.5" fill="none" stroke="#fff" stroke-width="1.8"/><path d="M6.5 11.3l3 3 6-6.3" fill="none" stroke="#fff" stroke-width="2"/></svg>
        <span>Service includes a 21 point inspection</span>
      </li>
    </ul>

    <h2 class="abs extras-title">Additional services:</h2>
    <ul class="abs extras">
      <li class="extra"><svg viewBox="0 0 13 13" aria-hidden="true"><circle cx="6.5" cy="6.5" r="6.5" fill="var(--teal)"/><path d="M3.5 6.7l2 2 4-4.2" fill="none" stroke="#fff" stroke-width="1.6"/></svg>Engine air filter replacement</li>
      <li class="extra"><svg viewBox="0 0 13 13" aria-hidden="true"><circle cx="6.5" cy="6.5" r="6.5" fill="var(--teal)"/><path d="M3.5 6.7l2 2 4-4.2" fill="none" stroke="#fff" stroke-width="1.6"/></svg>Cabine air filter replacement</li>
      <li class="extra"><svg viewBox="0 0 13 13" aria-hidden="true"><circle cx="6.5" cy="6.5" r="6.5" fill="var(--teal)"/><path d="M3.5 6.7l2 2 4-4.2" fill="none" stroke="#fff" stroke-width="1.6"/></svg>Wiperblade replacement</li>
      <li class="extra"><svg viewBox="0 0 13 13" aria-hidden="true"><circle cx="6.5" cy="6.5" r="6.5" fill="var(--teal)"/><path d="M3.5 6.7l2 2 4-4.2" fill="none" stroke="#fff" stroke-width="1.6"/></svg>Power steering fluid flush</li>
      <li class="extra"><svg viewBox="0 0 13 13" aria-hidden="true"><circle cx="6.5" cy="6.5" r="6.5" fill="var(--teal)"/><path d="M3.5 6.7l2 2 4-4.2" fill="none" stroke="#fff" stroke-width="1.6"/></svg>Fuel system treatment</li>
      <li class="extra"><svg viewBox="0 0 13 13" aria-hidden="true"><circle cx="6.5" cy="6.5" r="6.5" fill="var(--teal)"/><path d="M3.5 6.7l2 2 4-4.2" fill="none" stroke="#fff" stroke-width="1.6"/></svg>Brake fluid flush</li>
    </ul>
  </section>

  <footer>
    <div class="abs footer-item footer-web">
      <svg viewBox="0 0 20 20" aria-hidden="true"><circle cx="10" cy="10" r="10" fill="#fff"/><circle cx="10" cy="10" r="6" fill="none" stroke="var(--ink)" stroke-width="1.3"/><ellipse cx="10" cy="10" rx="2.6" ry="6" fill="none" stroke="var(--ink)" stroke-width="1.2"/><path d="M4 10h12" stroke="var(--ink)" stroke-width="1.2"/></svg>
      <span>www.brookmerelubeworks.com</span>
    </div>
    <div class="abs footer-item footer-mail">
      <svg viewBox="0 0 20 20" aria-hidden="true"><circle cx="10" cy="10" r="10" fill="#fff"/><rect x="5" y="6.5" width="10" height="7" fill="none" stroke="var(--teal)" stroke-width="1.3"/><path d="M5 6.8l5 4 5-4" fill="none" stroke="var(--teal)" stroke-width="1.3"/></svg>
      <span>sales@brookmerelubeworks.com</span>
    </div>
  </footer>
</article>
</body>
</html>
```